Business and Success Coaching Business Card

Need a business card for my coaching business. I coach small businesses, career professionals and, individuals wanting to unlock their human potential and achieve excellence. At the heart of our methodology is the Shaping Purposeful Action Routines Knowingly (SPARK) approach to formulate empowerment, create principles for success and setting achievable outcomes. I would like something that incorporates our new logo, something clean and sharp with a solid darker, but complementary background, color on the card front. The back should be white where there will be room for three questions

Target Market(s)

People looking to advance and improve themselves through a success coach

Industry/Entity Type

Life Coaching

Contact Information for Business Card

Contact information on card.
Business name on front of card
Questions on back

Font styles to use
Other font styles liked:
• Century Gothic or other Serif style fonts that look similar to Century Gothic

Colors

Designer to choose colors to be used in the design.

Requirements
Must have
• Logo on front of card
• Business name - The Steady Forge
• Contact name - Ted Harlow
• Address - Box 4619, Littleton, CO 80127-4619
• Phone number - 303-555-0147
• Email address - harlow.ted@thesteadyforge.example
• Certifications - CSC, CCHt, PTT, PNLP
• Back of card
• Three questions on the back of the card:
• If you were at your best, what would you do right now?
• What is the decision you have been avoiding?
• What's one action you could take in the next 10 minutes?
Nice to have
• I would like to see a solid color on the front of the card that compliments the logo.
• Back should be white, or could be contrasting, but need to have the three questions.

```html
<!DOCTYPE html>
<html lang="en">
<head>
<meta charset="utf-8">
<title>The Steady Forge – Business Card</title>
<link rel="stylesheet" href="https://fonts.googleapis.com/css2?family=Open+Sans:wght@700&family=Questrial&display=swap">
<style>
  :root {
    --backdrop: #e9e9e9;
    --navy: #22366a;
    --accent: #4a86c8;
    --white: #ffffff;
    --rule: #8a9bc0;
  }
  * { margin: 0; padding: 0; box-sizing: border-box; }
  html, body { width: 1200px; height: 900px; overflow: hidden; background: var(--backdrop); }
  body { position: relative; font-family: "Questrial", "Century Gothic", sans-serif; }

  .card { position: absolute; top: 297px; width: 514px; height: 306px; overflow: hidden; }
  .card--front { left: 67px; background: var(--navy); color: var(--white); }
  .card--back { left: 619px; background: var(--white); color: var(--navy); }

  .brand { position: absolute; display: flex; align-items: center; gap: 8px;
           font-family: "Open Sans", sans-serif; font-weight: 700; white-space: nowrap; }
  .brand__square { width: 14px; height: 14px; background: var(--accent); flex: none; }
  .card--front .brand { left: 139px; top: 172px; transform: translateX(-50%); font-size: 19px; color: var(--white); }
  .card--back .brand { left: 257px; top: 113px; transform: translateX(-50%); font-size: 21px; color: var(--navy); }

  .divider { position: absolute; left: 243px; top: 50px; width: 1px; height: 206px; background: var(--rule); }

  .person { position: absolute; left: 271px; top: 74px; padding-left: 21px; }
  .person::before { content: ""; position: absolute; left: 0; top: 2px; width: 12px; height: 34px; background: var(--accent); }
  .person__name { font-family: "Open Sans", sans-serif; font-weight: 700; font-size: 18px; letter-spacing: -0.2px; line-height: 22px; }
  .person__company { font-size: 14px; line-height: 18px; }

  .contacts { position: absolute; left: 276px; top: 133px; list-style: none; }
  .contacts li { display: flex; align-items: center; height: 20.8px; font-size: 11px; white-space: nowrap; }
  .contacts svg { width: 13px; height: 13px; margin-right: 10px; flex: none; }

  .questions { position: absolute; left: 38px; top: 175px; list-style: none; }
  .questions li { display: flex; align-items: center; height: 26px; font-size: 15.5px; white-space: nowrap; }
  .questions li::before { content: ""; width: 15px; height: 15px; background: var(--accent); margin-right: 6px; flex: none; }

  .back-band { position: absolute; left: 0; bottom: 0; width: 100%; height: 31px; background: var(--navy); }
</style>
</head>
<body>
  <section class="card card--front">
    <div class="brand"><span class="brand__square"></span>The Steady Forge</div>
    <div class="divider"></div>
    <div class="person">
      <div class="person__name">TED HARLOW</div>
      <div class="person__company">The Steady Forge</div>
    </div>
    <ul class="contacts">
      <li><svg viewBox="0 0 16 16"><path fill="#fff" d="M3 1l3 3-1.5 2a8 8 0 0 0 5.5 5.5L12 10l3 3-2 2C7 15 1 9 1 3z"/></svg>303-555-0147</li>
      <li><svg viewBox="0 0 16 16"><rect x="1" y="3.5" width="14" height="9" fill="none" stroke="#fff" stroke-width="1.4"/><path d="M1 3.5l7 5 7-5" fill="none" stroke="#fff" stroke-width="1.4"/></svg>harlow.ted@thesteadyforge.example</li>
      <li><svg viewBox="0 0 16 16"><rect x="1" y="2" width="12" height="11" fill="none" stroke="#fff" stroke-width="1.3"/><path d="M3 5h8M3 7.5h6M3 10h4" stroke="#fff" stroke-width="1.2"/><circle cx="12.5" cy="12" r="2.5" fill="#fff"/></svg>CSC, CCHt, PTT, PNLP</li>
      <li><svg viewBox="0 0 16 16"><path fill="#fff" d="M8 1a5 5 0 0 1 5 5c0 4-5 9-5 9S3 10 3 6a5 5 0 0 1 5-5zm0 3a2 2 0 1 0 0 4 2 2 0 0 0 0-4z"/></svg>Box 4619, Littleton, CO 80127-4619</li>
      <li><svg viewBox="0 0 16 16"><circle cx="8" cy="8" r="6.5" fill="none" stroke="#fff" stroke-width="1.3"/><ellipse cx="8" cy="8" rx="3" ry="6.5" fill="none" stroke="#fff" stroke-width="1.1"/><path d="M1.5 8h13M2.5 5h11M2.5 11h11" stroke="#fff" stroke-width="1"/></svg>www.thesteadyforge.example</li>
    </ul>
  </section>

  <section class="card card--back">
    <div class="brand"><span class="brand__square"></span>The Steady Forge</div>
    <ul class="questions">
      <li>If you were at your best, What would you do right now?</li>
      <li>What is the decision you have been avoiding?</li>
      <li>What's one action you could take in the next 10 minutes?</li>
    </ul>
    <div class="back-band"></div>
  </section>
</body>
</html>
```